Pilates Classes Flyer Design

I need a flyer designed that will promote my range of classes held in Bath, UK. I teach beginners, intermediate level and Over 50's and 60's and also teach individuals in their own homes. I would like to see designs using my colours blue Pantone 306 and Lime Green 14-0452 TPX TCX. The flyer should reflect a friendly, welcoming and professional class structure. I attach an old flyer for your reference and copy.

Target Market(s)

Men and Women who have busy lives working hard, who recognise they need to stretch out, do some exercise and de-stress after a busy day

Ladies over 50 who want to do some Pilates in a friendly fun environment and meet people at the same time.

Industry/Entity Type

It Professional

Font styles to use
Sans Serif
Script

Requirements
Must have
• One-sided flyer
Text only logo. Drop the figure

```html
<!DOCTYPE html>
<html lang="en">
<head>
<meta charset="utf-8">
<title>Stillpoint Pilates – New Classes Flyer</title>
<link href="https://fonts.googleapis.com/css2?family=Open+Sans:wght@400;600;700;800&family=Quicksand:wght@400;500;700&display=swap" rel="stylesheet">
<style>
  :root {
    --backdrop: #e9eef1;
    --paper-light: #ffffff;
    --paper-mid: #e6f3fa;
    --paper-edge: #bfe3f3;
    --ink: #1a5a7a;
    --ink-strong: #11506f;
    --brand-blue: #2aa3d6;
    --ribbon: #d4e3a6;
    --ribbon-shade: #b6cc84;
    --wave-deep: #13a6dc;
    --wave-mid: #3fbbe6;
    --wave-pale: #8dd6f1;
    --white: #ffffff;
  }
  * { box-sizing: border-box; margin: 0; padding: 0; }
  html, body { width: 1200px; height: 887px; overflow: hidden; }
  body {
    background: var(--backdrop);
    font-family: "Open Sans", Arial, sans-serif;
    color: var(--ink);
    position: relative;
  }
  .flyer {
    position: absolute;
    left: 348px; top: 46px;
    width: 550px; height: 796px;
    background: radial-gradient(ellipse at 50% 30%, var(--paper-light) 0%, var(--paper-mid) 60%, var(--paper-edge) 100%);
  }
  .decor-figure {
    position: absolute;
    right: 40px; top: 10px;
    width: 44px; height: 700px;
    background: linear-gradient(180deg, rgba(120,170,200,0.2), rgba(120,170,200,0.06));
    border-radius: 22px;
  }
  .brand {
    position: absolute; top: 38px; left: 0; width: 100%;
    text-align: center;
    font-weight: 400;
    color: var(--brand-blue);
    font-size: 30px;
    letter-spacing: 0.5px;
    line-height: 1;
  }
  .headline-ribbon { position: absolute; left: -14px; top: 126px; width: 550px; height: 90px; }
  .headline {
    position: absolute; left: 45px; top: 132px; width: 464px; height: 55px;
    background: var(--ribbon);
    color: var(--white);
    font-weight: 800; font-size: 33px;
    text-align: center; line-height: 55px;
    text-shadow: 0 1px 2px rgba(80,110,40,0.35);
  }
  .intro {
    position: absolute; top: 214px; left: 65px; width: 420px;
    text-align: center; font-size: 16.5px; line-height: 23px; color: var(--ink);
  }
  .features {
    position: absolute; top: 306px; left: 20px; width: 510px;
    text-align: center; font-size: 14px; line-height: 18px;
  }
  .features strong { font-weight: 700; color: var(--ink-strong); }
  .divider {
    position: absolute; left: 92px; width: 368px;
    border-top: 2px dotted rgba(26,90,122,0.55);
    z-index: 2;
  }
  .divider.top { top: 400px; }
  .divider.bottom { top: 578px; }
  .venues {
    position: absolute; top: 410px; left: 40px; width: 470px;
    text-align: center; font-size: 14px; line-height: 16px;
    z-index: 2;
  }
  .venues h2 { font-size: 14px; font-weight: 700; color: var(--ink-strong); margin-bottom: 14px; }
  .venue { margin-bottom: 14px; }
  .venue-name { font-weight: 600; color: var(--ink-strong); }
  .waves { position: absolute; left: 0; top: 556px; width: 550px; height: 240px; z-index: 1; }
  .contact {
    position: absolute; right: 22px; top: 704px;
    text-align: right; color: var(--white);
    font-family: "Quicksand", Arial, sans-serif;
    z-index: 2;
  }
  .contact .call { font-size: 25px; font-weight: 400; letter-spacing: 1px; }
  .contact .call b { font-weight: 700; letter-spacing: 1.5px; }
  .contact .email { font-size: 23px; font-weight: 700; letter-spacing: 1px; margin-top: 2px; }
</style>
</head>
<body>
  <main class="flyer">
    <div class="decor-figure" role="img" aria-label="Faint flowing decorative figure"></div>

    <div class="brand">Stillpoint Pilates</div>

    <svg class="headline-ribbon" viewBox="0 0 550 90" aria-hidden="true">
      <polygon points="0,40 60,40 60,80 0,80 18,60" fill="var(--ribbon-shade)"/>
      <polygon points="466,40 550,40 532,60 550,80 466,80" fill="var(--ribbon-shade)"/>
    </svg>
    <h1 class="headline">NEW CLASSES NEAR YOU!</h1>

    <p class="intro">Pilates is for EVERYONE whatever level of fitness, age or ability to help you build strength, flexibility and overall well-being</p>

    <div class="features">
      <p><strong>Quality teaching with Balanced Core Method Teacher.</strong></p>
      <p>Progressive approach. Teaching good movement skills.</p>
      <p><strong>Small class sizes and friendly atmosphere.</strong></p>
      <p>Beginners, Intermediate and Over 50's classes to choose from</p>
    </div>

    <div class="divider top"></div>
    <section class="venues">
      <h2>Join my one-hour classes at:</h2>
      <div class="venue"><div class="venue-name">St Aldric's Church Hall, Elm Rise</div><div>Monday evenings, Tuesday and Friday mornings.</div></div>
      <div class="venue"><div class="venue-name">Larkfield Dr. Surgery</div><div>Tuesday evenings.</div></div>
      <div class="venue"><div class="venue-name">Ashcombe Centre, Mill Road,</div><div>Wednesday mornings and evenings.</div></div>
    </section>
    <div class="divider bottom"></div>

    <svg class="waves" viewBox="0 0 550 240" preserveAspectRatio="none" aria-hidden="true">
      <path d="M0,55 C150,40 350,30 550,0 L550,240 L0,240 Z" fill="var(--wave-pale)"/>
      <path d="M0,78 C180,62 360,45 550,22 L550,240 L0,240 Z" fill="var(--wave-mid)"/>
      <path d="M0,120 C140,100 300,110 550,55 L550,240 L0,240 Z" fill="var(--wave-deep)"/>
      <path d="M0,90 C200,85 380,52 550,26" stroke="var(--white)" stroke-width="2" fill="none" opacity="0.7"/>
      <path d="M0,140 C180,115 330,130 550,85" stroke="var(--wave-pale)" stroke-width="3" fill="none" opacity="0.6"/>
    </svg>

    <div class="contact">
      <div class="call">Call Helen on <b>07700900123</b></div>
      <div class="email">helen.marsh@example.co.uk</div>
    </div>
  </main>
</body>
</html>
```